Halvex Land Surveying Website Design

We are working with Halvex. They are a national land surveying company and in need of a new website design.

Some sites to use for inspiration:

https://brantholmeng.com
https://www.pvdinc.com
https://lurendo.com
https://gwy.us
https://korvanbuilt.com
https://www.ferrisgalbrandi.com

Thank you for taking the time to consider designing a website for us. We are web developers based in Stockton and Los Angeles, CA, USA. Most of our projects go through the same process. Understanding this process may help you win a project with us. We custom-code all of our websites in-house. We don’t have any requirements as to what tools you use for your design, but we prefer Figma files. For any design that we label as four-stars, we send it to the client for review. The client picks the final design they want us to use. Once we complete this process, we will continue to show additional clients all the four-star sites and purchase them later. Your designs will have multiple chances to sell. For better chances of success, we ask that you follow these guidelines.

IMAGES:
If you use any images or icons in the design, we ask that you have a link to the asset so we can purchase the image/icon. Most of the designs we submit do not have the customer’s images on them unless they have some great images. Be creative; show us the feeling you are trying to portray with your image choices. Use any royalty-free site you choose. We subscribe to Quillo and mainly use their images, but we can purchase images outside of Quillo.

PLEASE NOTE: we will not submit designs to clients with watermarks on the images.

FONTS:
We ask that you identify the fonts used in the design. This can be done in a message if you want. We typically use Vexmar Fonts and Quillo Fonts.

CONTENT:
We're always open to different content and ideas. We often submit designs with stock images so the client can see our vision. We typically take pictures after the website launch to use their images with our vision. Lorem Ipsum is fine for paragraphs, but we ask that you write the headers in correct English. We want to be able to show the vision and identify the sections of the website.

INSPIRATION:
We typically add a couple of links in the brief of websites we like to help you get started in your design.

REVISIONS:
We do not often ask for revisions of the designs unless we see something in the design that may not appeal to the client. If there are slight changes that we want to make, we do that in the development process.

FEEDBACK:
We rarely give feedback on designs during the design process. We are working on many website projects and do not have the time to provide feedback. We usually respond if your request is well thought out and asks specific questions, but a note asking “feedback, please” usually goes unanswered.

```html
<!DOCTYPE html>
<html lang="en">
<head>
<meta charset="utf-8">
<title>Halvex Land Surveying</title>
<link href="https://fonts.googleapis.com/css2?family=Bebas+Neue&family=Montserrat:wght@400;500;600;700&display=swap" rel="stylesheet">
<style>
:root{
  --orange:#ee4a12;
  --orange-dark:#c9380a;
  --ink:#111111;
  --text:#6b6b6b;
  --light:#f4f4f4;
  --pink:#fde9e2;
  --footer:#1b1b1b;
  --white:#ffffff;
}
*{box-sizing:border-box;margin:0;padding:0}
html,body{width:1200px;height:3708px;overflow:hidden}
body{position:relative;background:var(--white);font-family:'Montserrat',sans-serif;color:var(--ink)}
.abs{position:absolute}
.display{font-family:'Bebas Neue',sans-serif;font-weight:400;line-height:1}
.btn{position:absolute;background:var(--orange);color:var(--white);font-family:'Montserrat',sans-serif;font-weight:700;font-size:12px;letter-spacing:.3px;display:flex;align-items:center;justify-content:center;text-transform:uppercase}

/* header */
.site-header{left:0;top:0;width:1200px;height:63px;background:var(--white)}
.brand{left:104px;top:14px;font-size:34px;color:var(--orange)}
.main-nav{left:466px;top:24px;display:flex;gap:20px;font-size:11.5px;color:#555;letter-spacing:.3px}
.main-nav span{display:flex;align-items:center;gap:4px}
.search-box{left:917px;top:16px;width:33px;height:32px;background:var(--ink);display:flex;align-items:center;justify-content:center}

/* hero */
.hero{left:0;top:63px;width:1200px;height:655px;background:linear-gradient(100deg,#3b4348 0%,#56615f 35%,#6b6f55 55%,#a65a22 78%,#d46a1e 100%)}
.hero-title-1{left:104px;top:228px;font-size:76px;color:var(--white)}
.hero-title-2{left:102px;top:290px;font-size:162px;color:var(--white)}
.hero-sub{left:104px;top:437px;font-size:23px;color:var(--white)}
.hero-arrows{left:104px;top:650px}

/* about */
.frame-pink{background:var(--pink)}
.photo{background:linear-gradient(135deg,#6d9a1e,#a9c93a 50%,#3e6b1a)}
.eyebrow{font-size:19px;color:var(--orange)}
.section-heading{font-size:40px;color:var(--ink);line-height:1}
.para{font-size:11.5px;line-height:19px;color:var(--text)}

/* stats */
.stats{left:104px;top:1245px;width:992px;height:125px;background:linear-gradient(90deg,var(--orange),#f26a32 50%,var(--orange-dark))}
.stat{position:absolute;top:18px;width:260px;text-align:center;color:var(--white)}
.stat .num{font-size:62px}
.stat .num sup{font-size:34px;vertical-align:top;position:relative;top:10px}
.stat .lbl{font-size:18px;margin-top:2px}

/* services */
.center-title{width:1200px;text-align:center}
.service-card{position:absolute;top:1546px;width:235px;height:369px;background:var(--light)}
.service-card .img{height:271px}
.service-card .badge{position:absolute;left:88px;top:247px;width:59px;height:52px;background:var(--orange);border:3px solid var(--white);display:flex;align-items:center;justify-content:center}
.service-card .name{position:absolute;left:0;top:313px;width:100%;text-align:center;font-size:18px;line-height:21px}

/* difference */
.diff-card{left:104px;top:2125px;width:460px;height:376px;background:var(--white);box-shadow:0 4px 24px rgba(0,0,0,.08)}
.feature{position:absolute;left:34px;width:366px;height:70px}
.feature .icon{position:absolute;left:0;top:0;width:59px;height:59px;background:var(--orange);display:flex;align-items:center;justify-content:center}
.feature .t{position:absolute;left:74px;top:6px;font-size:18px}
.feature .d{position:absolute;left:74px;top:28px;font-size:11px;color:var(--text)}
.feature .rule{position:absolute;left:74px;top:73px;width:292px;height:1px;background:#dcdcdc}

/* industries */
.industry{position:absolute;top:2689px;width:220px;height:127px;background:var(--light)}
.industry .icon{position:absolute;left:80px;top:19px;width:60px;height:60px;background:var(--orange);display:flex;align-items:center;justify-content:center}
.industry .name{position:absolute;left:0;top:94px;width:100%;text-align:center;font-size:18px}

/* footer */
.site-footer{left:0;top:3367px;width:1200px;height:341px;background:var(--footer);color:var(--white)}
.foot-head{font-size:27px;color:var(--white)}
.foot-links{font-size:12px;line-height:22.5px;color:#e6e6e6}
.social{position:absolute;top:3525px;width:43px;height:34px}
</style>
</head>
<body>

<header class="abs site-header">
  <div class="abs brand display">HALVEX</div>
  <nav class="abs main-nav">
    <span>LEGACY <svg width="8" height="6"><path d="M1 1l3 3 3-3" stroke="#555" fill="none"/></svg></span>
    <span>EXPERTISE <svg width="8" height="6"><path d="M1 1l3 3 3-3" stroke="#555" fill="none"/></svg></span>
    <span>PROJECTS <svg width="8" height="6"><path d="M1 1l3 3 3-3" stroke="#555" fill="none"/></svg></span>
    <span>CAREERS <svg width="8" height="6"><path d="M1 1l3 3 3-3" stroke="#555" fill="none"/></svg></span>
    <span>INSIGHTS</span>
  </nav>
  <div class="abs search-box"><svg width="13" height="13"><circle cx="5.5" cy="5.5" r="4" stroke="#fff" stroke-width="1.6" fill="none"/><path d="M8.5 8.5l3.5 3.5" stroke="#fff" stroke-width="1.6"/></svg></div>
  <div class="btn" style="left:957px;top:16px;width:139px;height:32px">CONTACT US</div>
</header>

<section class="abs hero" role="img" aria-label="Surveyor in hard hat and orange vest operating a total station on a tripod outdoors"></section>
<div class="abs hero-title-1 display">CONSTRUCTION</div>
<div class="abs hero-title-2 display">SUPPORT</div>
<div class="abs hero-sub display">STAKING, PROPERTY LINES, INSPECTIONS, AND MORE...</div>
<div class="btn" style="left:104px;top:483px;width:138px;height:31px">GET A QUOTE</div>
<svg class="abs hero-arrows" width="94" height="20"><path d="M2 10h38M2 10l7-6M2 10l7 6" stroke="#fff" stroke-width="1.8" fill="none"/><path d="M54 10h38M92 10l-7-6M92 10l-7 6" stroke="#fff" stroke-width="1.8" fill="none"/></svg>

<!-- about -->
<div class="abs frame-pink" style="left:181px;top:807px;width:405px;height:334px"></div>
<div class="abs photo" style="left:200px;top:823px;width:404px;height:331px" role="img" aria-label="Aerial view of a rural property with a stone house surrounded by green trees and fields"></div>
<div class="abs eyebrow display" style="left:652px;top:862px">ABOUT US</div>
<div class="abs section-heading display" style="left:650px;top:890px">OVER 25 YEARS OF TRUSTED<br>GENERAL CONTRACTING</div>
<p class="abs para" style="left:652px;top:976px;width:372px">Halvex is a leading national land surveying company providing comprehensive surveying and mapping solutions. Our team of experts combines decades of experience with the latest technology to deliver precise, reliable results for clients across industries.</p>
<div class="btn" style="left:650px;top:1088px;width:139px;height:32px">READ MORE</div>

<!-- stats -->
<div class="abs stats" role="img" aria-label="Orange band over a faint photo of surveyors at work"></div>
<div class="abs" style="left:104px;top:1245px;width:992px;height:125px">
  <div class="stat display" style="left:61px"><div class="num">140<sup>+</sup></div><div class="lbl">SUCCESS FUL PROJECTS</div></div>
  <div class="stat display" style="left:366px"><div class="num">35<sup>+</sup></div><div class="lbl">TEAM MEMBERS</div></div>
  <div class="stat display" style="left:667px"><div class="num">80<sup>+</sup></div><div class="lbl">HAPPY CLIENTS</div></div>
</div>

<!-- services -->
<h2 class="abs center-title display" style="left:0;top:1456px;font-size:36px">OUR SERVICES</h2>
<p class="abs center-title" style="left:0;top:1504px;font-size:12px;color:var(--text)">From boundary surveys to advanced geospatial mapping, we cover it all.</p>

<div class="service-card" style="left:104px">
  <div class="img" style="background:linear-gradient(160deg,#8fa7b5,#b77a3a 55%,#3b3f3a)" role="img" aria-label="Surveyors with a total station and tablet in the field"></div>
  <div class="badge"><svg width="30" height="30"><path d="M15 4l-9 22M15 4l9 22M15 4v22" stroke="#fff" stroke-width="2" fill="none"/><rect x="10" y="3" width="10" height="6" fill="#fff"/></svg></div>
  <div class="name display">BUNDARY &amp; TOPOGRAPHIC<br>SURVEYS</div>
</div>
<div class="service-card" style="left:357px">
  <div class="img" style="background:linear-gradient(170deg,#4d7a3a,#a8a43c 50%,#7f6a48)" role="img" aria-label="Surveyor in a safety vest behind a yellow tripod instrument in a grassy field"></div>
  <div class="badge"><svg width="30" height="30"><circle cx="15" cy="7" r="4" fill="#fff"/><path d="M15 11l-8 16M15 11l8 16M15 11v16" stroke="#fff" stroke-width="2" fill="none"/></svg></div>
  <div class="name display">ALTA/NSPS LAND TITLE<br>SURVEYS</div>
</div>
<div class="service-card" style="left:609px">
  <div class="img" style="background:linear-gradient(180deg,#7da846,#c9d2cf 45%,#5d6b5a)" role="img" aria-label="3D laser scanner mounted on a tripod outdoors"></div>
  <div class="badge"><svg width="30" height="30"><path d="M15 6l9 5v10l-9 5-9-5V11z" stroke="#fff" stroke-width="2" fill="none"/><path d="M6 11l9 5 9-5M15 16v10" stroke="#fff" stroke-width="2" fill="none"/></svg></div>
  <div class="name display">3D LASER SCANNING &amp;<br>MAPPING</div>
</div>
<div class="service-card" style="left:861px">
  <div class="img" style="background:linear-gradient(180deg,#4a90d0,#a9d3ef 45%,#4a8a6a 75%,#c48a30)" role="img" aria-label="Survey drone flying above a lake and forest"></div>
  <div class="badge"><svg width="30" height="30"><rect x="10" y="12" width="10" height="7" fill="#fff"/><path d="M4 9h8M18 9h8M8 9v4M22 9v4M8 13h14" stroke="#fff" stroke-width="2" fill="none"/><circle cx="15" cy="23" r="2" fill="#fff"/></svg></div>
  <div class="name display">DRONE AND AERIAL<br>SURVEYING</div>
</div>

<!-- difference -->
<div class="abs" style="left:482px;top:2017px;width:613px;height:517px;background:linear-gradient(110deg,#4b5a68,#7e8a7a 40%,#d0651d 70%,#3b3a36)" role="img" aria-label="Surveyor in hard hat and orange jacket looking through a total station"></div>
<div class="abs diff-card">
  <h2 class="abs display" style="left:34px;top:40px;font-size:36px">THE HALVEX DIFFERENCE</h2>
  <div class="feature" style="top:102px">
    <div class="icon"><svg width="34" height="34"><circle cx="17" cy="17" r="12" stroke="#fff" stroke-width="2" fill="none"/><circle cx="17" cy="17" r="6" stroke="#fff" stroke-width="2" fill="none"/><path d="M17 17l12-12" stroke="#fff" stroke-width="2"/></svg></div>
    <div class="t display">ACCURACY FIRST</div><div class="d">Every project backed by rigorous quality control.</div><div class="rule"></div>
  </div>
  <div class="feature" style="top:186px">
    <div class="icon"><svg width="34" height="34"><rect x="5" y="9" width="24" height="16" stroke="#fff" stroke-width="2" fill="none"/><path d="M5 29h24M12 5h10" stroke="#fff" stroke-width="2"/></svg></div>
    <div class="t display">NATIONWIDE REACH</div><div class="d">Serving clients across the United States.</div><div class="rule"></div>
  </div>
  <div class="feature" style="top:270px">
    <div class="icon"><svg width="34" height="34"><circle cx="17" cy="13" r="8" stroke="#fff" stroke-width="2" fill="none"/><path d="M13 23h8M14 27h6" stroke="#fff" stroke-width="2"/></svg></div>
    <div class="t display">INNOVATIVE TECHNOLOGY</div><div class="d">Using drones, 3D scanners, and GIS systems.</div>
  </div>
</div>

<!-- industries -->
<h2 class="abs center-title display" style="left:0;top:2627px;font-size:36px">TRUSTED BY INDUSTRIES NATIONWIDE</h2>
<div class="industry" style="left:138px"><div class="icon"><svg width="34" height="34"><rect x="7" y="5" width="12" height="24" stroke="#fff" stroke-width="2" fill="none"/><rect x="19" y="13" width="9" height="16" stroke="#fff" stroke-width="2" fill="none"/><path d="M10 10h6M10 15h6M10 20h6" stroke="#fff" stroke-width="2"/></svg></div><div class="name display">COMMERCIAL REAL ESTATE</div></div>
<div class="industry" style="left:373px"><div class="icon"><svg width="34" height="34"><path d="M7 27L27 7M7 7l20 20" stroke="#fff" stroke-width="3"/></svg></div><div class="name display">ENERGY AND UTILITIES</div></div>
<div class="industry" style="left:606px"><div class="icon"><svg width="34" height="34"><rect x="9" y="5" width="16" height="14" stroke="#fff" stroke-width="2" fill="none"/><path d="M5 23h24M9 23v6M25 23v6M17 19v10" stroke="#fff" stroke-width="2"/></svg></div><div class="name display">INFRASTRUCTURE</div></div>
<div class="industry" style="left:840px"><div class="icon"><svg width="34" height="34"><rect x="8" y="6" width="18" height="18" rx="3" stroke="#fff" stroke-width="2" fill="none"/><path d="M8 15h18" stroke="#fff" stroke-width="2"/><circle cx="12" cy="28" r="2" fill="#fff"/><circle cx="22" cy="28" r="2" fill="#fff"/></svg></div><div class="name display">TRANSPORTATION</div></div>

<!-- projects -->
<div class="abs frame-pink" style="left:167px;top:2914px;width:430px;height:332px"></div>
<div class="abs" style="left:186px;top:2930px;width:431px;height:332px;background:linear-gradient(180deg,#8fb3d6 0%,#6d8c6a 22%,#1f6fb5 35%,#1b5fa3 100%)" role="img" aria-label="Aerial view of a dredging barge with a yellow excavator on a blue bay"></div>
<div class="abs eyebrow display" style="left:667px;top:2962px">OUR PROJECTS</div>
<div class="abs section-heading display" style="left:666px;top:2999px">PROJECTS THAT REFLECT<br>OUR PURPOSE</div>
<p class="abs para" style="left:666px;top:3083px;width:372px">Halvex is a leading national land surveying company providing comprehensive surveying and mapping solutions. Our team of experts combines decades of experience with the latest technology to deliver precise, reliable results for clients across industries.</p>
<div class="btn" style="left:666px;top:3189px;width:180px;height:32px">BROWSE PROJECTS</div>
<div class="abs" style="left:853px;top:3189px;width:32px;height:32px;background:var(--ink);display:flex;align-items:center;justify-content:center"><svg width="14" height="14"><path d="M2 1h3l2 4-2 1.5c1 2 2 3 4 4L10.5 9l3.5 2v3c-7 0-12-5-12-12z" fill="#fff"/></svg></div>
<div class="abs" style="left:895px;top:3199px;font-size:11.5px;font-weight:700">HAVE QUESTIONS?</div>

<!-- footer -->
<footer class="abs site-footer"></footer>
<div class="abs display" style="left:104px;top:3458px;font-size:54px;color:var(--orange)">HALVEX</div>
<div class="social" style="left:130px;background:var(--orange)"></div>
<div class="social" style="left:180px;background:#3a3a3a"></div>
<div class="social" style="left:229px;background:#3a3a3a"></div>

<div class="abs foot-head display" style="left:381px;top:3439px">QUICK LINKS</div>
<div class="abs foot-links" style="left:381px;top:3476px">Legacy<br>Expertise<br>Projects<br>Careers<br>Insights</div>

<div class="abs foot-head display" style="left:591px;top:3439px">INFORMATION</div>
<div class="abs foot-links" style="left:591px;top:3476px">Terms &amp; Condition<br>Privacy Policy<br>Disclaimer<br>FAQ<br>Client Reviews</div>

<div class="abs foot-head display" style="left:807px;top:3439px">SUBSCRIBE TO OUR NEWSLETTER</div>
<div class="abs" style="left:807px;top:3483px;font-size:12px;color:#e6e6e6">hello@example.com</div>
<svg class="abs" style="left:1080px;top:3484px" width="14" height="14"><path d="M1 7l12-6-4 12-2-5z" fill="var(--orange)"/></svg>
<div class="abs" style="left:807px;top:3505px;width:289px;height:1px;background:#555"></div>
<div class="abs" style="left:807px;top:3519px;font-size:12px;color:#e6e6e6">*We don't spam</div>

<div class="abs" style="left:104px;top:3649px;width:992px;height:1px;background:#555"></div>
<div class="abs center-title" style="left:0;top:3670px;font-size:11.5px;color:#e6e6e6">© Copyright Halvex 2025. All Rights Reserved</div>
<div class="abs" style="left:1124px;top:3631px;width:42px;height:38px;background:var(--orange);display:flex;align-items:center;justify-content:center"><svg width="14" height="18"><path d="M7 17V2M2 7l5-5 5 5" stroke="#fff" stroke-width="1.8" fill="none"/></svg></div>

</body>
</html>
```